Wealth Management Business Card

We are a professional services consulting firm that specializes in high net worth individuals over $25,000,000, executives C-suite and above, closely held businesses owners, family offices and highly compensated employees.

Our focus is on risk mitigation and tax efficient strategies. Our clients take their risk on themselves and have a proven track record generating wealth. Our directive is to preserve and protect the wealth they’ve already created.

Our company Harbridge Advisory is geared around five directives of asset protection:
1) Legal Structuring
2) Leverage & Financing
3) Risk Management - Asset Protection & Insurance, Trustee Work
4) Asset Management & Investing - Under www.qelvantcapital.com
5) Tax Efficient Strategies

Our Company Mark is a Pentagon with a key in the middle. A pentagon is the most efficient defensive structure. Each point of a pentagon is equal distance front every point . Each side provides support to another and works together, which is the key to our clients success.

Our key colors are blue, black and silver.

We ‘re located in the Pacific Northwest with bi coastal and international clients. We have fewer, higher net worth clients and provide exceptional customer service. We do not do social media.

website is www.harbridgepath.com

Target Market(s)

High End Clients

Contact Information for Business Card

extra thick

Font styles to use
Serif

Requirements
Must have
• Metalic foil for lettering.
Black Background on one side
White Background on the other
Horizontal Format Only
No Rounded corners
Not Marketing sales information on the card.
Nice to have
• imprinted texture on the card
Should not have
• lots of color

```html
<!DOCTYPE html>
<html lang="en">
<head>
<meta charset="utf-8">
<title>Harbridge Advisory – Business Card</title>
<link rel="stylesheet" href="https://fonts.googleapis.com/css2?family=Cinzel:wght@500&family=Arimo:wght@400&display=swap">
<style>
  :root {
    --backdrop: #1c1c1e;
    --card-black: #0b0b0c;
    --card-white: #f1f1f3;
    --foil-blue: #1a7fd0;
    --deep-blue: #1f3f8f;
    --navy-text: #1e3a86;
    --silver: #e6e8ec;
    --divider: #2a2a2c;
  }
  * { box-sizing: border-box; margin: 0; padding: 0; }
  html, body {
    width: 1200px; height: 900px; overflow: hidden;
    background: var(--backdrop);
  }
  .canvas { position: relative; width: 1200px; height: 900px; }

  .card {
    position: absolute;
    width: 540px; height: 309px;
    box-shadow: 0 18px 40px rgba(0,0,0,.55);
  }

  /* Front: black side */
  .card-front {
    left: 40px; top: 500px;
    background: var(--card-black);
    display: flex;
  }
  .brand-panel {
    width: 245px;
    display: flex; align-items: center; justify-content: center; gap: 12px;
    padding: 0 16px;
  }
  .brand-mark {
    width: 14px; height: 14px; flex: none;
    background: var(--foil-blue);
  }
  .brand-name {
    font-family: "Cinzel", Georgia, serif;
    font-weight: 500; font-size: 21px; line-height: 1.2;
    color: var(--foil-blue);
    letter-spacing: .04em;
  }
  .divider {
    width: 1px; margin: 50px 0;
    background: var(--divider);
  }
  .details {
    flex: 1; padding: 62px 0 0 26px;
    font-family: "Arimo", Arial, sans-serif;
    color: var(--silver);
  }
  .person-name {
    font-family: "Cinzel", Georgia, serif;
    font-weight: 500; font-size: 19px;
    color: var(--foil-blue); letter-spacing: .02em;
  }
  .person-title { font-size: 13px; margin-top: 3px; }
  .contact-list { list-style: none; margin-top: 18px; font-size: 13px; }
  .contact-list li { display: flex; align-items: center; gap: 8px; margin-bottom: 4px; }
  .contact-icon { width: 13px; height: 13px; flex: none; }
  .address { font-size: 13px; line-height: 1.4; margin-top: 16px; }

  /* Back: white side */
  .card-back {
    left: 620px; top: 110px;
    background: var(--card-white);
  }
  .diagram { position: absolute; inset: 0; }
  .center-mark {
    position: absolute; left: 275px; top: 160px;
    transform: translate(-50%, -50%);
    display: flex; align-items: center; gap: 8px;
  }
  .center-mark .brand-name { color: var(--deep-blue); font-size: 15px; }
  .center-mark .brand-mark { width: 10px; height: 10px; background: var(--deep-blue); }
  .node {
    position: absolute; width: 52px; height: 52px;
    border-radius: 50%; background: #fff;
    box-shadow: 0 2px 6px rgba(30,58,134,.18);
    transform: translate(-50%, -50%);
    display: flex; align-items: center; justify-content: center;
  }
  .node svg { width: 26px; height: 26px; }
  .node-label {
    position: absolute;
    font-family: "Arimo", Arial, sans-serif;
    font-size: 12.5px; line-height: 15px;
    color: var(--navy-text); white-space: nowrap;
  }
  .node-label.centered { transform: translateX(-50%); }
</style>
</head>
<body>
<main class="canvas">

  <section class="card card-front" aria-label="Business card, black side">
    <div class="brand-panel">
      <span class="brand-mark"></span>
      <span class="brand-name">Harbridge<br>Advisory</span>
    </div>
    <div class="divider"></div>
    <div class="details">
      <h1 class="person-name">CORWIN ASHDALE</h1>
      <p class="person-title">Financial Strategist and Founder</p>
      <ul class="contact-list">
        <li>
          <svg class="contact-icon" viewBox="0 0 16 16"><path d="M4 1.5l2.2 2.6-1.3 1.6a9 9 0 0 0 5.4 5.4l1.6-1.3 2.6 2.2-1.6 2.2C7.5 14 2 8.5 1.8 3.1z" fill="var(--foil-blue)"/></svg>
          (503) 555-0148
        </li>
        <li>
          <svg class="contact-icon" viewBox="0 0 16 16"><rect x="1" y="3.5" width="14" height="9" fill="var(--foil-blue)"/><path d="M1 3.5l7 5 7-5" stroke="var(--card-black)" stroke-width="1.3" fill="none"/></svg>
          info@harbridgepath.com
        </li>
        <li>
          <svg class="contact-icon" viewBox="0 0 16 16" fill="none" stroke="var(--foil-blue)" stroke-width="1.3"><circle cx="8" cy="8" r="6.5"/><ellipse cx="8" cy="8" rx="3" ry="6.5"/><path d="M1.5 8h13M2.5 5h11M2.5 11h11"/></svg>
          www.harbridgepath.com
        </li>
      </ul>
      <p class="address">418 Alder Row, Suite 112,<br>Millbrook, OR 97099</p>
    </div>
  </section>

  <section class="card card-back" aria-label="Business card, white side">
    <div class="diagram">
      <div class="center-mark">
        <span class="brand-mark"></span>
        <span class="brand-name">Harbridge<br>Advisory</span>
      </div>

      <div class="node" style="left:210px; top:80px;">
        <svg viewBox="0 0 24 24" fill="none" stroke="var(--foil-blue)" stroke-width="1.5"><rect x="6" y="4" width="12" height="8"/><path d="M3 17h6l3 2h7l2-2"/></svg>
      </div>
      <span class="node-label" style="right:255px; top:38px;">Asset Management &amp; Investing</span>

      <div class="node" style="left:345px; top:80px;">
        <svg viewBox="0 0 24 24" fill="none" stroke="var(--deep-blue)" stroke-width="1.5"><path d="M6 3h9l3 3v15H6z"/><path d="M9 12h6M9 16h4"/></svg>
      </div>
      <span class="node-label" style="left:325px; top:38px;">Legal Structuring</span>

      <div class="node" style="left:170px; top:168px;">
        <svg viewBox="0 0 24 24" fill="none" stroke="var(--deep-blue)" stroke-width="1.5"><rect x="4" y="3" width="11" height="17"/><path d="M7 7h5M7 11h5M7 15h5"/><circle cx="18" cy="15" r="3.5" stroke="var(--foil-blue)"/></svg>
      </div>
      <span class="node-label" style="right:402px; top:160px;">Tax Efficient Strategies</span>

      <div class="node" style="left:390px; top:172px;">
        <svg viewBox="0 0 24 24" fill="none" stroke="var(--deep-blue)" stroke-width="1.5"><path d="M3 20h18M6 20v-6M11 20V9M16 20v-8"/><circle cx="17" cy="6" r="3" stroke="var(--foil-blue)"/></svg>
      </div>
      <span class="node-label centered" style="left:390px; top:204px;">Leverage &amp; Financing</span>

      <div class="node" style="left:275px; top:252px;">
        <svg viewBox="0 0 24 24" fill="none" stroke="var(--deep-blue)" stroke-width="1.5"><path d="M12 4l9 16H3z"/><path d="M12 10v5M12 17v1" stroke="var(--foil-blue)"/></svg>
      </div>
      <span class="node-label" style="right:305px; top:245px;">Risk Management</span>
    </div>
  </section>

</main>
</body>
</html>
```